Glint5Gate Photography Business Cards

We need a good general business card that we can hand to our clients. We will be doing embossed gloss cards.

Target Market(s)

Real estate / Business to business / professionals

```html
<!DOCTYPE html>
<html lang="en">
<head>
<meta charset="utf-8">
<title>Glint5Gate Photography – Business Card</title>
<link href="https://fonts.googleapis.com/css2?family=Montserrat:wght@400;600;700&display=swap" rel="stylesheet">
<style>
  :root {
    --page-bg: #ecebe8;
    --card-black: #222222;
    --gold: #d9aa2c;
    --gold-light: #f4e3a6;
    --gold-deep: #c08a12;
    --text-white: #ffffff;
  }
  html, body {
    margin: 0;
    padding: 0;
    width: 1200px;
    height: 995px;
    overflow: hidden;
    background: var(--page-bg);
    font-family: "Montserrat", Arial, sans-serif;
  }
  .canvas {
    position: relative;
    width: 1200px;
    height: 995px;
  }
  .business-card {
    position: absolute;
    left: 220px;
    top: 262px;
    width: 760px;
    height: 470px;
  }
  .card-shape {
    position: absolute;
    inset: 0;
    width: 760px;
    height: 470px;
  }
  .card-content {
    position: absolute;
    inset: 0;
    display: flex;
    flex-direction: column;
    align-items: center;
    color: var(--text-white);
    text-align: center;
  }
  .brand {
    margin-top: 118px;
    color: var(--gold);
    font-weight: 700;
    line-height: 1;
  }
  .brand-name {
    display: block;
    font-size: 46px;
    letter-spacing: 0.5px;
  }
  .brand-sub {
    display: block;
    margin-top: 4px;
    font-size: 16px;
    letter-spacing: 6px;
  }
  .person-name {
    margin: 44px 0 0;
    font-size: 26px;
    font-weight: 700;
    letter-spacing: 0.5px;
  }
  .person-role {
    margin: 4px 0 0;
    font-size: 23px;
    font-weight: 400;
    letter-spacing: 0.5px;
  }
  .contact-icons {
    display: flex;
    gap: 6px;
    margin-top: 34px;
  }
  .contact-icons svg {
    width: 20px;
    height: 20px;
  }
  .contact-list {
    list-style: none;
    margin: 10px 0 0;
    padding: 0;
    font-size: 18px;
    line-height: 1.3;
    font-weight: 400;
  }
</style>
</head>
<body>
<main class="canvas">
  <section class="business-card">
    <svg class="card-shape" viewBox="0 0 760 470" aria-hidden="true">
      <defs>
        <linearGradient id="goldFoil" x1="0" y1="0" x2="1" y2="1">
          <stop offset="0" stop-color="var(--gold-deep)"/>
          <stop offset="0.35" stop-color="var(--gold)"/>
          <stop offset="0.65" stop-color="var(--gold-light)"/>
          <stop offset="1" stop-color="var(--gold)"/>
        </linearGradient>
      </defs>
      <path class="card-body" fill="var(--card-black)"
        d="M0 58 q0-14 14-14 H222 q12 0 18-10 l14-22 q7-12 21-12 H490 q14 0 21 12 l14 22 q6 10 18 10 H746 q14 0 14 14 V456 q0 14-14 14 H14 q-14 0-14-14 Z"/>
      <path class="card-frame" fill="none" stroke="url(#goldFoil)" stroke-width="4"
        d="M42 72 H236 q10 0 16-9 l12-21 q6-11 19-11 H482 q13 0 19 11 l12 21 q6 9 16 9 H718 a14 14 0 0 0 14 14 V428 a14 14 0 0 0 -14 14 H42 a14 14 0 0 0 -14 -14 V86 a14 14 0 0 0 14 -14 Z"/>
    </svg>

    <div class="card-content">
      <div class="brand">
        <span class="brand-name">Glint5Gate</span>
        <span class="brand-sub">PHOTOGRAPHY</span>
      </div>

      <h1 class="person-name">PERSON’S NAME</h1>
      <p class="person-role">DESIGNATION</p>

      <div class="contact-icons" aria-hidden="true">
        <svg viewBox="0 0 20 20" class="icon-phone">
          <circle cx="10" cy="10" r="9" fill="none" stroke="var(--gold)" stroke-width="1.5"/>
          <path d="M7 5.5 l2 2.5 -1.2 1.2 q1 2 3 3 l1.2-1.2 2.5 2 -1.3 1.5 q-5 -0.5 -7.7-7.5 Z" fill="var(--gold)"/>
        </svg>
        <svg viewBox="0 0 20 20" class="icon-mail">
          <circle cx="10" cy="10" r="9" fill="none" stroke="var(--gold)" stroke-width="1.5"/>
          <rect x="5" y="6.5" width="10" height="7" fill="var(--gold)"/>
          <path d="M5 6.5 L10 10.5 L15 6.5" fill="none" stroke="var(--card-black)" stroke-width="1"/>
        </svg>
        <svg viewBox="0 0 20 20" class="icon-web">
          <circle cx="10" cy="10" r="9" fill="none" stroke="var(--gold)" stroke-width="1.5"/>
          <circle cx="10" cy="10" r="5.5" fill="none" stroke="var(--gold)" stroke-width="1.2"/>
          <ellipse cx="10" cy="10" rx="2.3" ry="5.5" fill="none" stroke="var(--gold)" stroke-width="1"/>
          <path d="M4.5 10 H15.5" stroke="var(--gold)" stroke-width="1"/>
        </svg>
      </div>

      <ul class="contact-list">
        <li class="contact-phone">+0 123 456 789</li>
        <li class="contact-email">info@yourmail.com</li>
        <li class="contact-web">www.yourcompany.com</li>
      </ul>
    </div>
  </section>
</main>
</body>
</html>
```